Web Page Design for Major Airline Consolidator

We need a new design for an airline consolidator based out of NY. We'd really like to get the design as quickly as possible.

Here is a *very* rough mockup of what the site could look like, along with 3 main competitor's sites. Needless to say, they want a design that looks much better than their competitors. Please note that the mockup is an idea only, feel free to enhance / improve upon it.

Mockup - https://plankrig.example/tolvemark/QHRnPzKw

Competitors:
- http://www.trelvan.example/
- http://www.munderbline.example/home2.html
- https://www.prosbek.example/index.php

Target Market(s)

target markets are identified in the mockup

Industry/Entity Type

Airline

Number of Pages Required

1 page

Requirements
Must have
• need space on the left side for a travel request form which is missing in the mockup. Form should have standard air booking fields (to, from, date arrival & departure, travel class, etc).

```html
<!DOCTYPE html>
<html lang="en">
<head>
<meta charset="utf-8">
<title>Halvern Tours – Airline Consolidator</title>
<link rel="stylesheet" href="https://fonts.googleapis.com/css2?family=Oswald:wght@400&family=PT+Sans:wght@400;700&display=swap">
<style>
:root{
  --blue:#0a87c9;
  --blue-dark:#0673ad;
  --ink:#3d3d3d;
  --muted:#6b6b6b;
  --line:#e2e2e2;
  --band:#f5f5f5;
  --dark:#333333;
  --footer:#050505;
  --white:#ffffff;
}
*{box-sizing:border-box;margin:0;padding:0}
html,body{width:1200px;height:2273px;overflow:hidden}
body{font-family:"PT Sans",Arial,sans-serif;color:var(--ink);background:var(--white);position:relative}
.wrap{position:absolute;left:173px;width:856px}

/* header */
.site-header{position:absolute;top:0;left:0;width:1200px;height:160px;border-bottom:4px solid #ececec}
.brand{position:absolute;left:173px;top:32px;display:flex;align-items:center;gap:12px}
.brand-mark{width:46px;height:46px;background:#7a7a7a;border-radius:50%}
.brand-name{font-family:"Oswald",Arial,sans-serif;font-size:34px;color:#6f6f6f;line-height:1}
.brand-tag{font-family:"Oswald",Arial,sans-serif;font-size:15px;color:#6f6f6f;margin-top:4px}
.account{position:absolute;left:893px;top:35px;font-size:15px;color:#555}
.search{position:absolute;left:858px;top:73px;width:171px;height:32px;border:1px solid var(--line);border-radius:3px;font-size:11px;color:#999;padding:8px 11px}
.search svg{position:absolute;right:12px;top:10px}
.main-nav{position:absolute;left:173px;top:130px;width:856px;height:56px;background:var(--blue);border-bottom:3px solid var(--blue-dark);display:flex;align-items:center;justify-content:space-between;padding:0 18px;font-family:"Oswald",Arial,sans-serif;font-size:15px;color:var(--white);z-index:2}

/* hero */
.hero{position:absolute;top:160px;left:0;width:1200px;height:497px;background:linear-gradient(90deg,#b9c2c6 0%,#d4d0c8 35%,#c9b9a8 55%,#8a8d92 80%,#c6c9cc 100%)}
.hero-arrow{position:absolute;top:222px;width:34px;height:34px;border-radius:50%;background:rgba(60,60,60,.6)}
.hero-arrow svg{position:absolute;left:11px;top:9px}
.hero-copy{position:absolute;left:595px;top:158px;color:var(--white)}
.hero-copy h1{font-family:"Oswald",Arial,sans-serif;font-weight:400;font-size:33px;line-height:1}
.rating{margin-top:18px;font-size:15px;display:flex;align-items:center;gap:14px}
.stars{color:#f2a32b;letter-spacing:2px;font-size:11px}
.stars span{color:#ddd}
.checks{list-style:none;margin-top:14px}
.checks li{font-size:15px;height:27px;display:flex;align-items:center;gap:13px}
.cta{display:inline-block;margin-top:12px;background:var(--blue);color:var(--white);font-size:15px;padding:12px 25px;border-radius:2px}
.quote-form{position:absolute;left:173px;top:347px;width:289px;height:326px;background:#f4f4f4;box-shadow:0 12px 16px rgba(0,0,0,.25);border-radius:3px;padding:16px 24px;z-index:2}
.quote-form h2{font-weight:400;font-size:20px;color:var(--blue);margin-bottom:12px}
.field{height:36px;background:var(--white);border:1px solid #e6e6e6;border-radius:3px;font-size:11px;color:#777;padding:11px 13px;margin-bottom:15px;position:relative}
.field svg{position:absolute;right:10px;top:14px}
.agree{display:flex;gap:8px;font-size:11px;color:#555;line-height:1.4;margin-top:-2px}
.box{width:14px;height:14px;border:1px solid #aaa;background:var(--white);flex:none;margin-top:2px}
.btn-dark{display:inline-block;background:var(--dark);color:var(--white);font-size:14px;padding:9px 14px;border-radius:3px}
.quote-form .btn-dark{margin-top:12px}

/* audiences */
.section-title{position:absolute;left:0;width:1200px;text-align:center;font-size:24px;color:#444}
.cards{top:768px;display:flex;justify-content:space-between}
.card{width:267px}
.card-head{height:60px;border:1px solid var(--line);border-bottom:none;background:#fafafa;padding:9px 11px}
.card-head h3{font-weight:400;font-size:16px;color:#444}
.card-head p{font-size:11px;color:#555;margin-top:4px}
.card-photo{height:176px}
.ticks{list-style:none;margin-top:16px}
.ticks li{font-size:12.5px;color:#555;height:27px;display:flex;align-items:center;gap:10px}
.card .btn-dark{margin-top:9px;padding:8px 14px}

/* trust band */
.trust{position:absolute;top:1183px;left:0;width:1200px;height:95px;background:var(--band);border-top:1px solid #ececec;border-bottom:1px solid #ececec}
.trust-label{position:absolute;left:272px;top:37px;font-size:16px;color:var(--blue)}
.badge{position:absolute;background:#b3b3b3}

/* business */
.biz{top:1315px;height:273px}
.biz-photo{position:absolute;left:0;top:0;width:296px;height:273px}
.biz-copy{position:absolute;left:325px;top:0}
.biz-copy h2{font-weight:400;font-size:21px;color:#444}
.biz-copy .lead{font-size:15px;color:#555;margin-top:10px}
.biz-copy ul{list-style:none;margin-top:12px}
.biz-copy li{font-size:15px;color:#555;line-height:29px}
.btn-blue{display:inline-block;background:var(--blue);color:var(--white);font-size:15px;padding:11px 25px;border-radius:2px;margin-top:12px}

/* group */
.group{position:absolute;top:1630px;left:0;width:1200px;height:283px;background:var(--band)}
.group h2{position:absolute;top:22px;width:1200px;text-align:center;font-weight:400;font-size:20px;color:#222}
.offer{position:absolute;top:84px;width:410px;height:166px}
.offer-photo{position:absolute;left:0;top:0;width:181px;height:166px}
.offer h3{position:absolute;left:202px;top:0;font-weight:400;font-size:15px;color:#333}
.offer p{position:absolute;left:202px;top:30px;width:208px;font-size:11.5px;color:#666;line-height:20px;text-align:justify}
.btn-outline{position:absolute;left:197px;top:130px;border:1px solid var(--blue);color:var(--blue);font-size:14px;padding:7px 11px;border-radius:3px;background:var(--white)}

/* testimonial */
.testimonial{top:1954px;height:182px}
.ceo-photo{position:absolute;left:0;top:5px;width:182px;height:182px;border-radius:50%;background:radial-gradient(circle at 50% 40%,#9fb6c6 0%,#6e7c86 60%,#4b4f53 100%)}
.quote{position:absolute;left:232px;top:6px;width:600px;font-size:11.5px;line-height:20px;color:#555}
.qmark{position:absolute;font-family:Georgia,serif;font-size:34px;color:#999;line-height:1}
.sign{position:absolute;left:223px;top:78px;font-size:13px;color:#555;line-height:20px}
.links{position:absolute;left:212px;top:141px;display:flex;gap:10px}
.links span{border:1px solid #bbb;border-radius:3px;font-size:14px;color:#444;padding:7px 18px}

/* footer */
.site-footer{position:absolute;top:2172px;left:0;width:1200px;height:101px;background:var(--footer);color:#999}
.copy{position:absolute;left:173px;top:26px;font-size:12px}
.foot-nav{position:absolute;left:173px;top:61px;font-size:11.5px;display:flex;gap:8px}
.social{position:absolute;left:940px;top:39px;display:flex;gap:5px}
.social i{width:25px;height:25px;border-radius:50%;display:block}
</style>
</head>
<body>

<header class="site-header">
  <div class="brand">
    <span class="brand-mark"></span>
    <div>
      <div class="brand-name">Halvern Tours</div>
      <div class="brand-tag">The Professional's choice since 1974</div>
    </div>
  </div>
  <div class="account">My Account / Login</div>
  <div class="search">Search
    <svg width="11" height="11" viewBox="0 0 11 11"><circle cx="4.5" cy="4.5" r="3.5" fill="none" stroke="#999" stroke-width="1.4"/><line x1="7" y1="7" x2="10" y2="10" stroke="#999" stroke-width="1.4"/></svg>
  </div>
</header>

<nav class="main-nav">
  <span>Home</span><span>Travel Agencies</span><span>Religious &amp; Group Travel</span><span>Corporate Concierge</span><span>Niche Agencies</span><span>Destinations</span><span>About</span><span>Restricted Area</span>
</nav>

<section class="hero" role="img" aria-label="Photo of smiling business travel agents in an office">
  <span class="hero-arrow" style="left:33px"><svg width="10" height="16" viewBox="0 0 10 16"><polyline points="8,2 2,8 8,14" fill="none" stroke="#fff" stroke-width="2"/></svg></span>
  <span class="hero-arrow" style="left:1129px"><svg width="10" height="16" viewBox="0 0 10 16"><polyline points="2,2 8,8 2,14" fill="none" stroke="#fff" stroke-width="2"/></svg></span>
  <div class="hero-copy">
    <h1>More Than Just Airline Consolidation</h1>
    <div class="rating"><span class="stars">★★★<span>●●</span></span>Check out our reviews!</div>
    <ul class="checks">
      <li><svg width="12" height="12" viewBox="0 0 12 12"><circle cx="6" cy="6" r="6" fill="#fff"/><polyline points="3,6 5.2,8.2 9,4" fill="none" stroke="#555" stroke-width="1.5"/></svg>We're here for our clients!</li>
      <li><svg width="12" height="12" viewBox="0 0 12 12"><circle cx="6" cy="6" r="6" fill="#fff"/><polyline points="3,6 5.2,8.2 9,4" fill="none" stroke="#555" stroke-width="1.5"/></svg>Over 40 years in business</li>
      <li><svg width="12" height="12" viewBox="0 0 12 12"><circle cx="6" cy="6" r="6" fill="#fff"/><polyline points="3,6 5.2,8.2 9,4" fill="none" stroke="#555" stroke-width="1.5"/></svg>Locations across the USA</li>
      <li><svg width="12" height="12" viewBox="0 0 12 12"><circle cx="6" cy="6" r="6" fill="#fff"/><polyline points="3,6 5.2,8.2 9,4" fill="none" stroke="#555" stroke-width="1.5"/></svg>50+ air carriers</li>
      <li><svg width="12" height="12" viewBox="0 0 12 12"><circle cx="6" cy="6" r="6" fill="#fff"/><polyline points="3,6 5.2,8.2 9,4" fill="none" stroke="#555" stroke-width="1.5"/></svg>Worldwide + Europe &amp; Middle East travel</li>
    </ul>
    <span class="cta">Get Access Today!</span>
  </div>
</section>

<form class="quote-form">
  <h2>Request Quotes</h2>
  <div class="field">From</div>
  <div class="field">Date arrival &amp; departure<svg width="8" height="5" viewBox="0 0 8 5"><polyline points="1,1 4,4 7,1" fill="none" stroke="#777" stroke-width="1.2"/></svg></div>
  <div class="field">Travel Class<svg width="8" height="5" viewBox="0 0 8 5"><polyline points="1,1 4,4 7,1" fill="none" stroke="#777" stroke-width="1.2"/></svg></div>
  <div class="agree"><span class="box"><svg width="12" height="12" viewBox="0 0 12 12"><polyline points="2.5,6 5,8.5 9.5,3" fill="none" stroke="#444" stroke-width="1.5"/></svg></span>I have read and I agreed with<br>Terms &amp; Conditions</div>
  <span class="btn-dark">AIR BOOKING</span>
</form>

<h2 class="section-title" style="top:709px">Airline Consolidator for Travel Agents</h2>

<section class="wrap cards">
  <article class="card">
    <div class="card-head"><h3>Home Based Travel Agents</h3><p>Find your way to financial freedom!</p></div>
    <div class="card-photo" role="img" aria-label="Photo of a family in front of their house" style="background:linear-gradient(180deg,#b9d1e6 0%,#c9b8a4 45%,#6f9a4a 100%)"></div>
    <ul class="ticks">
      <li><svg width="9" height="9" viewBox="0 0 9 9"><polyline points="1,4.5 3.5,7 8,1.5" fill="none" stroke="#555" stroke-width="1.5"/></svg>don't lose another client to the big guys</li>
      <li><svg width="9" height="9" viewBox="0 0 9 9"><polyline points="1,4.5 3.5,7 8,1.5" fill="none" stroke="#555" stroke-width="1.5"/></svg>get more referrals and more customers!</li>
      <li><svg width="9" height="9" viewBox="0 0 9 9"><polyline points="1,4.5 3.5,7 8,1.5" fill="none" stroke="#555" stroke-width="1.5"/></svg>earn more per sale!</li>
    </ul>
    <span class="btn-dark">Join Now</span>
  </article>
  <article class="card">
    <div class="card-head"><h3>Small Travel Agencies</h3><p>Accelerate your growth!</p></div>
    <div class="card-photo" role="img" aria-label="Photo of a small travel agency team" style="background:linear-gradient(180deg,#eef2f5 0%,#d8d3cd 50%,#3a3a3e 100%)"></div>
    <ul class="ticks">
      <li><svg width="9" height="9" viewBox="0 0 9 9"><polyline points="1,4.5 3.5,7 8,1.5" fill="none" stroke="#555" stroke-width="1.5"/></svg>reason #1</li>
      <li><svg width="9" height="9" viewBox="0 0 9 9"><polyline points="1,4.5 3.5,7 8,1.5" fill="none" stroke="#555" stroke-width="1.5"/></svg>reason #2</li>
      <li><svg width="9" height="9" viewBox="0 0 9 9"><polyline points="1,4.5 3.5,7 8,1.5" fill="none" stroke="#555" stroke-width="1.5"/></svg>reason #3</li>
    </ul>
    <span class="btn-dark">Join Now</span>
  </article>
  <article class="card">
    <div class="card-head"><h3>Corporate Travel Agencies</h3><p>Earn &amp; retain higher value clients</p></div>
    <div class="card-photo" role="img" aria-label="Photo of a corporate agent with a headset and colleagues" style="background:linear-gradient(135deg,#f1ece4 0%,#d9c6ae 45%,#7c90b0 100%)"></div>
    <ul class="ticks">
      <li><svg width="9" height="9" viewBox="0 0 9 9"><polyline points="1,4.5 3.5,7 8,1.5" fill="none" stroke="#555" stroke-width="1.5"/></svg>reason #1</li>
      <li><svg width="9" height="9" viewBox="0 0 9 9"><polyline points="1,4.5 3.5,7 8,1.5" fill="none" stroke="#555" stroke-width="1.5"/></svg>reason #2</li>
      <li><svg width="9" height="9" viewBox="0 0 9 9"><polyline points="1,4.5 3.5,7 8,1.5" fill="none" stroke="#555" stroke-width="1.5"/></svg>reason #3</li>
    </ul>
    <span class="btn-dark">Join Now</span>
  </article>
</section>

<section class="trust">
  <span class="trust-label">Trusted Members of :</span>
  <span class="badge" style="left:452px;top:27px;width:107px;height:42px;border-radius:2px"></span>
  <span class="badge" style="left:619px;top:17px;width:68px;height:62px;border-radius:50%"></span>
  <span class="badge" style="left:754px;top:20px;width:90px;height:56px;border-radius:4px"></span>
</section>

<section class="wrap biz">
  <div class="biz-photo" role="img" aria-label="Photo of call-centre agents wearing headsets" style="background:linear-gradient(135deg,#f4f1ed 0%,#c9ad94 40%,#3b3d44 100%)"></div>
  <div class="biz-copy">
    <h2>Airline Consolidators for Businesses &amp; Corporations</h2>
    <p class="lead">Tired of Travel Headaches? Make Business Travel EASY!</p>
    <ul>
      <li>*E*xcellent customer service, we staff over 200 agents and have locations in</li>
      <li>6 major US cities &nbsp;*A*lways available ...</li>
      <li>buy in bulk &amp; save even more!</li>
      <li>*S*ave more by going direct to the consolidator!</li>
      <li>*Y*our best interests are ours!</li>
    </ul>
    <span class="btn-blue">Experience the difference of Halvern!</span>
  </div>
</section>

<section class="group">
  <h2>Group Travel - Missionary Airfares, HAJJ &amp; Umra Discounted Airfares</h2>
  <div class="offer" style="left:173px">
    <div class="offer-photo" role="img" aria-label="Photo of a family group dressed for pilgrimage" style="background:linear-gradient(180deg,#9aa58a 0%,#6a5c52 50%,#2e2a2a 100%)"></div>
    <h3>HAJJ Group Travel Rates</h3>
    <p>Lorem ipsum dolor sit amet, consectetuer adipiscing elit, sed diam nonummy nibh euismod tincidunt ut laoreet dolore Lorem ipsum</p>
    <span class="btn-outline">CONTACT US NOW!</span>
  </div>
  <div class="offer" style="left:623px">
    <div class="offer-photo" role="img" aria-label="Photo of a missionary with children outdoors" style="background:linear-gradient(180deg,#8c9a6a 0%,#b8a37e 55%,#7a6a52 100%)"></div>
    <h3>Missionary Travel</h3>
    <p>Lorem ipsum dolor sit amet, consectetuer adipiscing elit, sed diam nonummy nibh euismod tincidunt ut laoreet dolore Lorem ipsum</p>
    <span class="btn-outline">CONTACT US NOW!</span>
  </div>
</section>

<section class="wrap testimonial">
  <div class="ceo-photo" role="img" aria-label="Portrait of the company president in a suit"></div>
  <span class="qmark" style="left:198px;top:0">&ldquo;</span>
  <p class="quote">Lorem ipsum dolor sit amet, consectetur adipiscing elit, sed do eiusmod tempor incididunt ut labore et dolore magna aliqua. Ut enim ad minim veniam, quis nostrud exercitation ullamco laboris nisi ut aliquip ex ea commodo consequat. Duis aute irure dolor in reprehenderit in voluptate velit esse cillum dolore eu fugiat nulla pariatur.</p>
  <span class="qmark" style="left:817px;top:53px">&rdquo;</span>
  <div class="sign">Mr. Dorvane<br>President &amp; CEO</div>
  <div class="links"><span>Our History</span><span>Our Divisions</span><span>Our employees</span></div>
</section>

<footer class="site-footer">
  <div class="copy">©2014 Halvern Tours Inc , All Rights Reserved.</div>
  <div class="foot-nav"><span>Home</span>|<span>Travel Agencies</span>|<span>Religious &amp; Group Travel</span>|<span>Corporate Concierge</span>|<span>Niche Agencies</span>|<span>Destinations</span>|<span>Contact Us</span></div>
  <div class="social"><i style="background:#3b5b9a"></i><i style="background:#2aa3d8"></i><i style="background:#c4302b"></i></div>
</footer>

</body>
</html>
```